Business Card and Letterhead for Nurlo - modern real estate business

I need a double sided business card design for Nurlo. Please see business card brief here https://papers.trelvimo.net/sheet/q/7XrTbaLeZpMmQ2uWvd9HkCj4yNoEfsGi3lRtAz_pk/view?mode=shared

Please feel free to design the business cards however you feel best. I am happy to give some creative freedoms and then provide feedback from there.

Please then also create a letterhead to match the business card design

Colors

Designer to choose colors to be used in the design.

Requirements
Must have
• Must be a modern, elegant business card which looks very professional

```html
<!DOCTYPE html>
<html lang="en">
<head>
<meta charset="utf-8">
<title>Nurlo – Business Card</title>
<link href="https://fonts.googleapis.com/css2?family=Raleway:wght@400;500;700&display=swap" rel="stylesheet">
<style>
  :root {
    --page: #ffffff;
    --card: #0c0c0c;
    --brand-red: #c4242b;
    --ink-light: #f2f2f2;
    --rule: #e8e8e8;
  }
  * { margin: 0; padding: 0; box-sizing: border-box; }
  html, body {
    width: 1200px;
    height: 801px;
    overflow: hidden;
    background: var(--page);
    font-family: "Raleway", sans-serif;
  }
  .stage {
    position: relative;
    width: 1200px;
    height: 801px;
  }
  .card {
    position: absolute;
    left: 372px;
    width: 471px;
    height: 302px;
    background: var(--card);
    overflow: hidden;
  }
  .card--front { top: 82px; }
  .card--back  { top: 454px; }

  /* Front */
  .front-wordmark {
    position: absolute;
    left: 0;
    width: 100%;
    top: 72px;
    text-align: center;
    color: var(--brand-red);
    font-weight: 700;
    font-size: 100px;
    line-height: 1;
    letter-spacing: 10px;
  }
  .front-rule {
    position: absolute;
    left: 20px;
    right: 20px;
    top: 178px;
    height: 2px;
    background: var(--rule);
  }
  .tagline {
    position: absolute;
    left: 0;
    width: 100%;
    top: 193px;
    text-align: center;
    font-size: 22px;
    font-weight: 400;
    letter-spacing: 3.2px;
    color: var(--ink-light);
    white-space: nowrap;
  }
  .tagline__accent {
    color: var(--brand-red);
    font-weight: 500;
  }

  /* Back */
  .portrait {
    position: absolute;
    left: 0;
    top: 0;
    width: 200px;
    height: 302px;
    background:
      linear-gradient(180deg, #ececec 0%, #c9cfc6 16%, #9aa58a 40%, #6f7660 62%, #2f2f2f 74%, #262626 100%);
  }
  .info-panel {
    position: absolute;
    left: 200px;
    top: 0;
    width: 271px;
    height: 302px;
  }
  .back-wordmark {
    position: absolute;
    left: 15px;
    right: 15px;
    top: 12px;
    text-align: center;
    color: var(--brand-red);
    font-weight: 700;
    font-size: 56px;
    line-height: 1;
    letter-spacing: 6px;
  }
  .back-rule {
    position: absolute;
    left: 0;
    right: 16px;
    top: 76px;
    height: 2px;
    background: var(--rule);
  }
  .agent-name {
    position: absolute;
    left: 17px;
    top: 109px;
    font-size: 25px;
    font-weight: 500;
    letter-spacing: 2.4px;
    color: var(--ink-light);
    line-height: 1;
  }
  .agent-title {
    position: absolute;
    left: 17px;
    top: 140px;
    font-size: 15.5px;
    letter-spacing: 1.1px;
    color: var(--ink-light);
    line-height: 1;
  }
  .contact {
    position: absolute;
    left: 17px;
    top: 180px;
    list-style: none;
    font-size: 15px;
    letter-spacing: 1.3px;
    line-height: 19.6px;
    color: var(--ink-light);
  }
  .contact__web {
    margin-top: 2px;
    color: var(--brand-red);
  }
</style>
</head>
<body>
  <main class="stage">
    <section class="card card--front">
      <div class="front-wordmark">NURLO</div>
      <div class="front-rule"></div>
      <p class="tagline">PROPERTY SOLD WITH <span class="tagline__accent">PURPOSE</span></p>
    </section>

    <section class="card card--back">
      <div class="portrait" role="img" aria-label="Portrait photograph of the agent in a dark suit, with a leafy valley view behind"></div>
      <div class="info-panel">
        <div class="back-wordmark">NURLO</div>
        <div class="back-rule"></div>
        <h1 class="agent-name">DEAN MARSH</h1>
        <p class="agent-title">Licenced Real Estate Agent</p>
        <ul class="contact">
          <li>0400 318 592</li>
          <li>dean@nurlo.com</li>
          <li>PO Box 1180</li>
          <li>Brenwood NSW 2790</li>
          <li class="contact__web">www.nurlo.com</li>
        </ul>
      </div>
    </section>
  </main>
</body>
</html>
```